Business card and stationary design
Lindora Development
Business card and stationary design -
Creative Brief
Simple
Marike Holzner - van Brugt
MSc, Dipl. Coach & Consultant
Feldrainweg 14 6318 Talmatt Switzerland
info@lindoradevelopment.ch
www.lindoradevelopment.ch
We're not sure about the font-type, could be the Logo-type or something that's compatible
Personal Coaching Health Coaching Business Coaching Consultancy out of the box, into the outdoors

```html
<!DOCTYPE html>
<html lang="en">
<head>
<meta charset="utf-8">
<title>Lindora Development – Stationery</title>
<link href="https://fonts.googleapis.com/css2?family=Montserrat:wght@400;600&display=swap" rel="stylesheet">
<style>
:root{
  --bg:#2a2a2c;
  --paper:#ffffff;
  --blue:#1b5ea9;
  --blue-deep:#0f3f7d;
  --sky:#49a7dc;
  --green:#8cc63f;
  --green-deep:#3f9a3a;
  --ink:#4a4a4a;
  --faint:#e3eef7;
}
*{margin:0;padding:0;box-sizing:border-box}
html,body{width:1200px;height:310px;overflow:hidden;background:var(--bg);font-family:"Montserrat",Arial,sans-serif;color:var(--ink)}
.canvas{position:relative;width:1200px;height:310px}
.item{position:absolute;background:var(--paper);overflow:hidden;box-shadow:0 2px 6px rgba(0,0,0,.45)}
.item svg.wave{position:absolute;left:0;width:100%}
.mark{display:flex;align-items:center;gap:4px;font-weight:600;color:var(--blue);white-space:nowrap}
.mark .dot{border-radius:50%;background:var(--blue);flex:none}
.brand{position:absolute;left:12px;top:10px;width:190px;text-align:center}
.brand .dot-lg{width:56px;height:56px;border-radius:50%;background:var(--blue);margin:0 auto 8px}
.brand .name{font-weight:600;color:var(--sky);font-size:12px;letter-spacing:1px;text-transform:uppercase}
.brand .sub{font-size:6px;color:#9aa;margin-top:4px}
.card{width:112px;height:54px}
.card-green{background:linear-gradient(135deg,var(--green) 0%,#5fb547 60%,var(--green-deep) 100%)}
.card-blue{background:linear-gradient(135deg,var(--sky),var(--blue) 60%,var(--blue-deep))}
.tiny{font-size:3.4px;line-height:5px;color:var(--ink);white-space:nowrap}
.watermark{position:absolute;border-radius:50%;background:var(--faint)}
.env-flap{position:absolute;left:0;top:0;width:100%;height:100%}
</style>
</head>
<body>
<div class="canvas">

  <div class="brand">
    <div class="dot-lg"></div>
    <div class="name">Lindora Development</div>
    <div class="sub">Business Cards</div>
  </div>

  <!-- business cards -->
  <div class="item card card-green" style="left:14px;top:118px">
    <div class="mark" style="position:absolute;left:30px;top:20px;font-size:6px;color:#fff"><span class="dot" style="width:10px;height:10px;background:#fff"></span>Lindora</div>
  </div>
  <div class="item card" style="left:136px;top:118px">
    <svg class="wave" style="top:0;height:100%" viewBox="0 0 112 54" preserveAspectRatio="none"><path d="M76 0 Q100 27 86 54 L112 54 L112 0Z" fill="var(--green)"/><path d="M86 0 Q106 27 96 54 L112 54 L112 0Z" fill="var(--blue)"/></svg>
    <div class="mark" style="position:absolute;left:8px;top:8px;font-size:5px"><span class="dot" style="width:8px;height:8px"></span>Lindora Development</div>
    <div class="tiny" style="position:absolute;left:8px;top:24px">Marike Holzner - van Brugt<br>MSc, Dipl. Coach &amp; Consultant<br>info@lindoradevelopment.ch<br>www.lindoradevelopment.ch</div>
  </div>
  <div class="item card" style="left:14px;top:204px">
    <svg class="wave" style="bottom:0;height:24px" viewBox="0 0 112 24" preserveAspectRatio="none"><path d="M0 12 Q56 0 112 14 L112 24 L0 24Z" fill="var(--sky)"/><path d="M0 18 Q60 8 112 20 L112 24 L0 24Z" fill="var(--blue)"/></svg>
    <div class="mark" style="position:absolute;left:8px;top:8px;font-size:5px"><span class="dot" style="width:8px;height:8px"></span>Lindora Development</div>
  </div>
  <div class="item card card-blue" style="left:136px;top:204px">
    <div class="mark" style="position:absolute;left:28px;top:20px;font-size:6px;color:#fff"><span class="dot" style="width:10px;height:10px;background:#fff"></span>Lindora</div>
  </div>

  <!-- letterhead with side wave -->
  <div class="item" style="left:271px;top:19px;width:132px;height:274px">
    <div class="watermark" style="left:30px;top:90px;width:72px;height:72px"></div>
    <div class="mark" style="position:absolute;left:34px;top:22px;font-size:6px"><span class="dot" style="width:12px;height:12px"></span>Lindora Development</div>
    <div class="tiny" style="position:absolute;right:10px;top:44px">Feldrainweg 14 6318<br>Talmatt Switzerland<br>info@lindoradevelopment.ch</div>
    <svg class="wave" style="top:0;height:100%" viewBox="0 0 132 274" preserveAspectRatio="none"><path d="M0 0 L14 0 Q2 130 10 274 L0 274Z" fill="var(--blue)"/><path d="M0 220 Q70 240 132 210 L132 274 L0 274Z" fill="var(--sky)" opacity=".85"/><path d="M0 246 Q70 258 132 238 L132 274 L0 274Z" fill="var(--blue)"/></svg>
  </div>

  <!-- letterhead centred -->
  <div class="item" style="left:425px;top:19px;width:132px;height:274px">
    <div class="watermark" style="left:30px;top:96px;width:72px;height:72px"></div>
    <div class="mark" style="position:absolute;left:36px;top:22px;font-size:6px"><span class="dot" style="width:12px;height:12px"></span>Lindora Development</div>
    <svg class="wave" style="bottom:0;height:34px" viewBox="0 0 132 34" preserveAspectRatio="none"><path d="M0 18 Q66 4 132 20 L132 34 L0 34Z" fill="var(--green)"/><path d="M0 26 Q70 14 132 28 L132 34 L0 34Z" fill="var(--blue)"/></svg>
  </div>

  <!-- compliment slip -->
  <div class="item" style="left:701px;top:19px;width:168px;height:124px">
    <div class="watermark" style="left:66px;top:40px;width:44px;height:44px"></div>
    <div class="mark" style="position:absolute;left:20px;top:14px;font-size:5px"><span class="dot" style="width:10px;height:10px"></span>Lindora Development</div>
    <div class="tiny" style="position:absolute;right:10px;top:14px">info@lindoradevelopment.ch<br>www.lindoradevelopment.ch</div>
    <svg class="wave" style="top:0;height:100%" viewBox="0 0 168 124" preserveAspectRatio="none"><path d="M0 0 L12 0 Q2 60 8 124 L0 124Z" fill="var(--blue)"/><path d="M0 104 Q84 92 168 108 L168 124 L0 124Z" fill="var(--sky)"/></svg>
  </div>

  <!-- small envelope -->
  <div class="item" style="left:701px;top:173px;width:168px;height:110px">
    <div class="mark" style="position:absolute;left:12px;top:10px;font-size:5px"><span class="dot" style="width:10px;height:10px"></span>Lindora Development</div>
    <svg class="wave" style="bottom:0;height:30px" viewBox="0 0 168 30" preserveAspectRatio="none"><path d="M0 14 Q84 2 168 18 L168 30 L0 30Z" fill="var(--green)"/><path d="M0 22 Q90 12 168 24 L168 30 L0 30Z" fill="var(--blue)"/></svg>
  </div>

  <!-- coloured envelope -->
  <div class="item" style="left:900px;top:48px;width:276px;height:96px;background:linear-gradient(180deg,var(--green),var(--sky) 55%,var(--blue))">
    <svg class="env-flap" viewBox="0 0 276 96" preserveAspectRatio="none"><path d="M0 0 L138 46 L276 0Z" fill="#fff" opacity=".18"/></svg>
    <span style="position:absolute;right:16px;top:16px;width:14px;height:14px;border-radius:50%;background:#fff"></span>
  </div>

  <!-- white envelope -->
  <div class="item" style="left:900px;top:168px;width:276px;height:115px">
    <svg class="env-flap" viewBox="0 0 276 115" preserveAspectRatio="none"><path d="M0 0 L138 62 L276 0" fill="none" stroke="#d6d6d6" stroke-width="1"/><path d="M0 115 L120 52 M276 115 L156 52" fill="none" stroke="#e2e2e2" stroke-width="1"/><path d="M0 0 L60 0 Q20 40 0 70Z" fill="var(--blue)"/><path d="M276 0 L216 0 Q256 40 276 70Z" fill="var(--green)"/></svg>
  </div>

</div>
</body>
</html>
```